Larkfield Circuitry LLC is a Minneapolis / St Paul and surrounding communities computer repair and service company. It serves residential and small businesses. We work primarily with virus removal, data recovery, system baselines, networking, and new system installation. The site should look clean, professional, and easy to navigate.

This wordpress project must be coded and integrated into a wordpress theme for easy upload and maintenance.
Updates

Designers - Please make sure your design is in a wordpress theme so that It can be uploaded.  

Thank you,

Brin 

Target Market(s)

Residential and Small Business

Industry/Entity Type

Residential

Requirements
Must have
• Site Content
1. Main Page should have photos that scroll across, Business Description, Space to run
“Specials” Ads
a. Intuitive Navigation
2. Additional Pages
a. Blog for Computer Repair Articles
b. Testimonials Page
c. Contact Pages
d. Services Page with the ability to put in pricing
3. The site must be clean and professional.
4. Wordpress Theme

```html
<!DOCTYPE html>
<html lang="en">
<head>
<meta charset="utf-8">
<title>Larkfield Circuitry LLC</title>
<link rel="stylesheet" href="https://fonts.googleapis.com/css2?family=Montserrat:wght@400;500;600&family=Open+Sans:wght@400;600&family=Lora:ital@1&display=swap">
<style>
:root{
  --green:#3f9a1c;
  --green-dark:#2f7d10;
  --page-bg:#eeeeee;
  --panel:#ffffff;
  --border:#d8d8d8;
  --text:#4a4a4a;
  --link:#1c8fc9;
  --ad-red:#d02f32;
  --ad-blue:#1f4f9a;
  --sea-deep:#1b86c4;
  --sea-light:#59c3ea;
  --tile-fill:#e9ecee;
}
*{box-sizing:border-box;margin:0;padding:0}
html,body{width:1114px;height:1200px;overflow:hidden}
body{background:var(--page-bg);font-family:"Open Sans",Arial,sans-serif;color:var(--text);position:relative}
.abs{position:absolute}

/* header */
.brand{left:131px;top:13px;height:67px;display:flex;align-items:center;gap:12px}
.brand-mark{width:64px;height:64px;border:4px solid var(--green);border-radius:50%}
.brand-name{font-family:"Montserrat",sans-serif;font-weight:600;font-size:27px;color:#555;line-height:1.05;width:230px}
.contact-top{left:696px;top:22px;width:285px}
.contact-row{display:flex;align-items:center;gap:14px}
.contact-row.phone{font-family:"Montserrat",sans-serif;font-size:19px;color:#444;border-bottom:1px solid #ddd;height:36px;padding-bottom:2px}
.contact-row.email{font-size:12.5px;color:var(--green);height:22px;margin-top:3px}

/* panel */
.panel{left:122px;top:88px;width:872px;height:932px;background:var(--panel);border:1px solid var(--border);border-radius:6px}

/* nav */
.nav{left:131px;top:98px;width:854px;height:33px;border-radius:6px;background:linear-gradient(#5cb631,var(--green-dark));display:flex;align-items:center;padding-left:12px;box-shadow:0 2px 0 #2a6a0d}
.nav a{font-family:"Montserrat",sans-serif;font-weight:500;color:#fff;text-decoration:none;font-size:14.5px;margin-right:19px;white-space:nowrap}
.search{left:739px;top:103px;width:240px;height:22px;background:#fff;border-radius:11px;display:flex;justify-content:flex-end;overflow:hidden}
.search svg{position:absolute;left:8px;top:5px}
.search-btn{width:60px;background:linear-gradient(#f4f4f4,#d8d8d8);font-size:12px;color:#333;display:flex;align-items:center;justify-content:center;border-left:1px solid #bbb}

/* hero */
.hero{left:130px;top:147px;width:855px;height:328px;border:1px solid var(--border);border-radius:4px;padding:5px}
.hero-image{width:100%;height:100%;background:linear-gradient(160deg,var(--sea-light),var(--sea-deep) 60%,#126ea8)}
.hero-caption{left:595px;top:267px;width:324px;height:90px;background:rgba(60,150,210,.55);border:1px solid rgba(255,255,255,.5);color:#fff;font-family:"Montserrat",sans-serif;font-weight:600;text-align:center;padding-top:12px}
.hero-caption .l1{font-size:37px;line-height:38px}
.hero-caption .l2{font-size:29px;line-height:30px}

/* welcome */
.welcome{left:148px;top:502px;width:545px}
.welcome-kicker{font-family:"Lora",serif;font-style:italic;font-size:18px;color:#777;line-height:18px}
.welcome-title{font-family:"Montserrat",sans-serif;font-weight:500;font-size:22px;color:var(--green);line-height:26px;margin-bottom:14px}
.welcome p{font-size:12.2px;line-height:17.4px;margin-bottom:17px}

/* service tiles */
.services{left:147px;top:843px;display:flex;gap:28px}
.tile{width:115px;height:145px;border:1px solid #e2e2e2;border-radius:4px;overflow:hidden}
.tile-art{height:92px;background:var(--tile-fill)}
.tile-label{height:53px;background:var(--green);color:#fff;font-family:"Montserrat",sans-serif;font-weight:500;font-size:14.5px;line-height:17px;padding:8px 9px}

/* ad */
.ad{left:723px;top:504px;width:262px;height:217px;border:4px solid var(--ad-red);background:#fff;text-align:center;font-family:"Montserrat",sans-serif}
.ad-headline{color:var(--ad-red);font-weight:600;font-size:30px;line-height:38px;margin-top:12px}
.ad-product{margin:8px auto 0;width:220px;height:46px;background:var(--ad-blue);border-radius:8px;color:#fff;font-weight:600;font-size:26px;line-height:46px}
.ad-sub{color:var(--ad-blue);font-weight:600;font-size:16px;margin-top:6px}
.ad-price{color:var(--ad-red);font-size:16px;margin-top:2px}

/* blog */
.blog-head{left:723px;top:740px;width:262px;height:34px;border:1px solid #ddd;border-radius:4px;background:linear-gradient(#fff,#eee);font-family:"Montserrat",sans-serif;font-weight:500;font-size:14.5px;color:#222;padding:8px 12px;box-shadow:0 2px 2px rgba(0,0,0,.12)}
.blog{left:723px;top:791px;width:255px;font-size:12px}
.blog-title{color:var(--link);font-size:12.5px;line-height:15px;margin-bottom:6px}
.blog-meta{color:#888;font-size:11.5px;line-height:16px}
.blog-author,.blog-date{color:#333;font-size:12.5px;line-height:19px}
.blog-excerpt{padding-left:2px;margin-top:2px;line-height:17.4px;font-size:12.2px}
.blog-more{color:var(--green);font-size:12.5px;margin-top:6px;padding-left:2px}

/* footer */
.footer{left:0;top:1055px;width:1114px;height:145px;background:linear-gradient(var(--green-dark),var(--green) 50%,#3c9516);border-top:2px solid #2b6c0d;color:#fff}
.footer h4{font-family:"Montserrat",sans-serif;font-weight:500;font-size:13px;position:absolute;top:21px}
.footer .col{position:absolute;font-size:12.2px;line-height:20px}
.social{display:flex;align-items:center;gap:11px;height:29px}
.social span.sq{width:19px;height:19px;background:#cfe6f5;border-radius:2px}
</style>
</head>
<body>

<header>
  <div class="abs brand">
    <span class="brand-mark"></span>
    <span class="brand-name">Larkfield Circuitry LLC</span>
  </div>
  <div class="abs contact-top">
    <div class="contact-row phone">
      <svg width="18" height="18" viewBox="0 0 18 18"><rect width="18" height="18" rx="3" fill="#3f9a1c"/><path d="M5 4c1 0 1.6 2 1.6 2.6 0 .6-.8 1-.8 1 .5 1.6 1.7 2.8 3.3 3.4 0 0 .4-.8 1-.8.6 0 2.6.6 2.6 1.6 0 1-1 1.7-1.8 1.7C7.6 13.5 4.5 10.4 4.5 6.2c0-1 .5-2.2.5-2.2z" fill="#fff"/></svg>
      <span>555-014-2290</span>
    </div>
    <div class="contact-row email">
      <svg width="18" height="14" viewBox="0 0 18 14"><rect width="18" height="14" rx="2" fill="#3f9a1c"/><path d="M2 3l7 5 7-5" stroke="#fff" stroke-width="1.6" fill="none"/></svg>
      <span>CustomerService@LarkfieldCircuitry.com</span>
    </div>
  </div>
</header>

<div class="abs panel"></div>

<nav class="abs nav">
  <a>Home</a><a>About Us</a><a>Services</a><a>Products</a><a>Blog</a><a>Testimonials</a><a>Contact Us</a>
</nav>
<div class="abs search">
  <svg width="12" height="12" viewBox="0 0 12 12"><circle cx="5" cy="5" r="3.6" stroke="#777" stroke-width="1.6" fill="none"/><path d="M7.6 7.6l3 3" stroke="#777" stroke-width="1.8"/></svg>
  <span class="search-btn">Search</span>
</div>

<section class="abs hero">
  <div class="hero-image" role="img" aria-label="Laptop resting on a life ring floating in clear blue water"></div>
</section>
<div class="abs hero-caption"><div class="l1">LOREM IPSUM</div><div class="l2">DOLOR SIT AMET</div></div>

<main class="abs welcome">
  <div class="welcome-kicker">Welcome to</div>
  <h1 class="welcome-title">Larkfield Circuitry LLC</h1>
  <p>Larkfield Circuitry LLC is proud to serve St. Paul, Minneapolis, and the surrounding area. We specialize in computer repair, networking, new system design, and can help solve many of your technology based needs. When you do business with Larkfield Circuitry LLC rest assured know that you're getting quality service with an organization dedicated to integrity, customer service, and fair pricing. We treat ever job big or small, residential or commercial, with the same level of commitment and vigor.</p>
  <p>Unlike much of our competition we provide an onsite technician to discuss your needs and diagnose potential problems. If we can't fix your problem onsite or it requires more in-depth diagnostics we will bring it to our shop and return it with absolutely no charge for transportation. If we can't fix your problem we will completely refund your initial diagnostic fee and any other service charges that might be incurred.</p>
  <p>Please note that there is a $60.00 onsite diagnostic fee of which half will be applied to your final bill if you elect to remedy your issues with Larkfield Circuitry LLC.</p>
</main>

<section class="abs services">
  <div class="tile"><div class="tile-art" role="img" aria-label="Service badge for virus removal"></div><div class="tile-label">Virus<br>Removal</div></div>
  <div class="tile"><div class="tile-art" role="img" aria-label="Service badge for data recovery"></div><div class="tile-label">Data<br>Recovery</div></div>
  <div class="tile"><div class="tile-art" role="img" aria-label="Service badge for system baselines"></div><div class="tile-label">System<br>Baselines</div></div>
  <div class="tile"><div class="tile-art" role="img" aria-label="Service badge for new system installation"></div><div class="tile-label">New System<br>Installation</div></div>
</section>

<aside class="abs ad">
  <div class="ad-headline">Cloud Suite<br>expensive?</div>
  <div class="ad-product">PostRelay</div>
  <div class="ad-sub">Business Email System</div>
  <div class="ad-price">Just $1 per user /mo</div>
</aside>

<div class="abs blog-head">Latest Blog Feeds</div>
<section class="abs blog">
  <div class="blog-title">Lorem ipsum dolor sit amet, consectetur adipiscing elit.</div>
  <div class="blog-meta">Posted by:</div>
  <div class="blog-author">Marion Tate</div>
  <div class="blog-date">03 Aug, 2012</div>
  <p class="blog-excerpt">Lorem ipsum dolor sit amet, consectetur adipisicing elit, sed do eiusmod tempor incididunt ut labore et dolore magna aliqua. Ut enim ad minim veniam, quis nostrud exercitation ullamco laboris nisi ut aliquip ex ea commodo consequat.</p>
  <div class="blog-more">View All +</div>
</section>

<footer class="abs footer">
  <h4 style="left:130px">Quick Navigation</h4>
  <div class="col" style="left:130px;top:44px">Home<br>About Us<br>Services<br>Products</div>
  <div class="col" style="left:218px;top:44px">Blog<br>Testimonials<br>Contact Us</div>
  <h4 style="left:321px">Contact Info</h4>
  <div class="col" style="left:321px;top:44px;line-height:18px">123 Lorem ipsum dolor<br>Some City, P.O 457845, Country<br><br><span style="line-height:22px">P:&nbsp; 555-014-2290</span><br>E:&nbsp; CustomerService@LarkfieldCircuitry.com</div>
  <h4 style="left:615px">Connect with us</h4>
  <div class="col" style="left:615px;top:45px">
    <div class="social"><span class="sq"></span>Join Us on FriendSpace</div>
    <div class="social"><span class="sq"></span>Chirper</div>
  </div>
  <h4 style="left:798px">© 2012 Larkfield Circuitry LLC</h4>
  <div class="col" style="left:798px;top:78px;line-height:16px">All right are reserved.<br>Terms of Service | Privacy Policy</div>
</footer>

</body>
</html>
```